Real Estate Sales and Marketing brochures

I have a few templates I uploaded of my old presentations and what I would like to see as a new presentation. I need 1 buyer (7-10 slides), 1 seller (8-12 slides), and 1 about me|us (4-5 slides) presentation. Those 3 would most likely contain 1-2 of the same slides and be 7-10 slides away. I would like it in power point presentation as well as pdf.

I am looking for something very clean, consistent, crisp, bright pictures (of the North Ga area.. Lake Lanier, North Ga Mtns, and the town of Forsyth County along with some really nice homes as the background). I have permission to use this photographers photos (he is my photographer). http://www.brennoquillfoto.com (go to interiors and exteriors) and http://blog.brennoquillfoto.com

The goal is to WoW people like my friends presentation labeled TRM does and 1: tell them what they will get with the list their home with us 2: when the buy with us and 3: who we are and what we have accomplished.

If I can get going in the right direction I would like to add stationary, letterhead, etc. to the order. My goal is to have great presentations and then have my flyers and all other printed materials match.

Target Market(s)

Buyers, sellers, and investors in the Real Estate Industry.

Industry/Entity Type

Real Estate Agent

Font styles to use
Serif

Colors
f04a50
85acd3

Requirements
Must have
• 1. about us 2. our services 3. our achievements 4. the process 5. about HV.
• Over 100m in sales (numbers and other awards can be seen at homeswithdarvel.com). Voted Finest of Pellham Valley by our Clients, 141,000 total votes, in the Pellham Valley Ledger. North Ga's sole Realtor for Property Guides We Rely On program.
Nice to have
• NICE clean pictures as the background
Should not have
• Dates on any logos or information other than achievements

```html
<!DOCTYPE html>
<html lang="en">
<head>
<meta charset="utf-8">
<title>The Home Selling Process</title>
<link rel="stylesheet" href="https://fonts.googleapis.com/css2?family=Crimson+Pro:ital,wght@0,300;0,400;0,500;1,400;1,500&display=swap">
<style>
  :root {
    --photo-dark: #2b2420;
    --photo-mid: #6b5a4c;
    --photo-light: #b9ad9c;
    --marble: #f2f1ef;
    --side-bar: #2f2f31;
    --panel: rgba(44, 44, 46, 0.84);
    --panel-edge: #1e1e1e;
    --text-light: #ffffff;
    --brand-red: #f04a50;
    --brand-blue: #85acd3;
  }
  html, body {
    margin: 0;
    padding: 0;
    overflow: hidden;
    background: #ffffff;
  }
  .slide {
    position: relative;
    width: 1200px;
    height: 675px;
    overflow: hidden;
    font-family: "Crimson Pro", Georgia, serif;
    color: var(--text-light);
  }
  .interior-photo {
    position: absolute;
    left: 0; top: 0;
    width: 891px; height: 675px;
    background:
      radial-gradient(ellipse at 55% 8%, #e8e2d6 0%, rgba(232,226,214,0) 35%),
      radial-gradient(ellipse at 30% 55%, #d9d2c6 0%, rgba(217,210,198,0) 30%),
      linear-gradient(180deg, var(--photo-light) 0%, var(--photo-mid) 45%, #4a3528 75%, var(--photo-dark) 100%);
  }
  .marble-strip {
    position: absolute;
    left: 891px; top: 0;
    width: 220px; height: 675px;
    background: linear-gradient(160deg, #fafafa 0%, var(--marble) 50%, #e7e6e4 100%);
  }
  .side-bar {
    position: absolute;
    left: 1111px; top: 0;
    width: 89px; height: 675px;
    background: var(--side-bar);
  }
  .content-panel {
    position: absolute;
    left: 321px; top: 100px;
    width: 879px; height: 520px;
    background: var(--panel);
    border: 1px solid var(--panel-edge);
    border-right: none;
    box-sizing: border-box;
  }
  .title {
    position: absolute;
    left: 9px; top: 8px;
    margin: 0;
    font-weight: 300;
    font-size: 40px;
    line-height: 48px;
    letter-spacing: 0.3px;
  }
  .body-copy {
    position: absolute;
    left: 9px;
    width: 860px;
    margin: 0;
    font-size: 18px;
    line-height: 23.5px;
    white-space: nowrap;
  }
  .intro { top: 113px; }
  .value { top: 220px; }
  .factors-heading { top: 292px; }
  .factor-list {
    position: absolute;
    left: 9px; top: 315px;
    margin: 0; padding: 0;
    list-style: none;
    font-size: 18px;
    line-height: 21px;
  }
  .factor-list li::before {
    content: "•";
    display: inline-block;
    width: 28px;
    color: var(--brand-blue);
  }
  .guarantee {
    position: absolute;
    left: 20px; top: 443px;
    width: 850px;
    margin: 0;
    text-align: center;
    font-style: italic;
    font-weight: 500;
    font-size: 16px;
    line-height: 21px;
    color: var(--brand-red);
  }
</style>
</head>
<body>
<div class="slide">
  <div class="interior-photo" role="img" aria-label="Bright open-plan home interior with dark hardwood floors, dark kitchen cabinets, white sofas and a fireplace"></div>
  <div class="marble-strip"></div>
  <div class="side-bar"></div>

  <section class="content-panel">
    <h1 class="title">THE HOME SELLING PROCESS</h1>
    <p class="body-copy intro">Getting top dollar for your house begins with understanding how to see your house through the eyes of a<br>buyer. <em>To be a successful seller you must have your house looking its best!</em> Tackle those items that could<br>affect your selling price or time on the market.</p>
    <p class="body-copy value">The value of your property is determined by what a BUYER is willing to pay in today’s market<br>based on comparing your property to others SOLD in your area.</p>
    <p class="body-copy factors-heading">5 Factors That Affect the Value of Your Property</p>
    <ul class="factor-list">
      <li>Location</li>
      <li>Market</li>
      <li>Terms</li>
      <li>Condition</li>
      <li>Price</li>
    </ul>
    <p class="guarantee">As Real Estate professionals dedicated to providing a level of service that is unsurpassed in the<br>Atlanta market, we are offering you, the SELLER, a Personal Performance Guarantee that outlines what you can expect<br>from us.</p>
  </section>
</div>
</body>
</html>
```